Employee I.D. Card - Badge

We need an employee I.D. card designed. Our employees are going to be wearing these. I would like to have it look nice. Something professional yet cool (not uptight if that makes sense).
Project Scope:
Vertical orientation
Company name ------------- (Bright and Tidy)
Website ------------- (brightandtidymn.example)
Employee Picture
background check image
front and back designed - same design on either side
You can create the card without having the employee images on them.
Here are the dimensions -
2.125 x 3.370 inches
Double sided - same design can be used front and back
Background badge - I would like to add an image that shows that the employee has taken a background check. I've added the press-kit for the company we use. If you have a better idea than incorporating their logo, we can certainly do something different.
Example image-
https://www.findwell-search.example/results?q=background+check+badge&mode=images
The print company will set up the names.
Logo is attached
Also attached are our business cards. You can use this for an idea of brand/company style.
Our website - brightandtidymn.example

```html
<!DOCTYPE html>
<html lang="en">
<head>
<meta charset="utf-8">
<title>Bright and Tidy – Employee ID Card</title>
<link rel="stylesheet" href="https://fonts.googleapis.com/css2?family=Arimo:wght@400;700&display=swap">
<style>
  :root {
    --page-bg: #e9e7e3;
    --card-bg: #ffffff;
    --brand-blue: #1b86d1;
    --brand-blue-light: #2aaee6;
    --brand-blue-dark: #176bbd;
    --brand-green: #8cc63f;
    --brand-green-light: #b3d335;
    --text-grey: #8a8c8e;
    --photo-frame: #c9c9c9;
    --badge-dark: #1f1f1f;
    --badge-gold: #c9a23a;
  }
  * { margin: 0; padding: 0; box-sizing: border-box; }
  html, body {
    width: 1200px;
    height: 900px;
    overflow: hidden;
    background: var(--page-bg);
    font-family: "Arimo", Arial, sans-serif;
  }
  .card-set {
    position: relative;
    width: 1200px;
    height: 900px;
  }
  .id-card {
    position: absolute;
    top: 82px;
    width: 430px;
    height: 738px;
    background: var(--card-bg);
    border-radius: 44px 6px 44px 6px;
    overflow: hidden;
    box-shadow: 0 4px 14px rgba(0,0,0,0.18);
  }
  .id-card--front { left: 127px; }
  .id-card--back { left: 643px; }

  .brand-name {
    position: absolute;
    top: 40px;
    left: 0;
    width: 100%;
    text-align: center;
    font-weight: 700;
    font-size: 68px;
    line-height: 76px;
    letter-spacing: -1px;
    color: var(--brand-blue);
  }
  .website {
    position: absolute;
    top: 234px;
    left: 0;
    width: 100%;
    text-align: center;
    font-size: 24px;
    font-weight: 400;
    color: var(--text-grey);
  }
  .website .part-blue { color: var(--brand-blue); }
  .website .part-green { color: var(--brand-green); }

  .employee-photo {
    position: absolute;
    top: 288px;
    left: 133px;
    width: 164px;
    height: 193px;
    border: 2px solid var(--photo-frame);
    border-radius: 10px;
    background: linear-gradient(180deg, #d8d6d4 0%, #a89888 45%, #3a3f48 100%);
  }
  .employee-name {
    position: absolute;
    top: 492px;
    left: 0;
    width: 100%;
    text-align: center;
    font-weight: 700;
    font-size: 36px;
    color: var(--brand-blue);
  }
  .employee-title {
    position: absolute;
    top: 534px;
    left: 0;
    width: 100%;
    text-align: center;
    font-weight: 700;
    font-size: 21px;
    color: var(--brand-green);
  }
  .band-blue {
    position: absolute;
    top: 615px;
    left: 0;
    width: 100%;
    height: 68px;
    background: linear-gradient(90deg, var(--brand-blue-light), var(--brand-blue-dark));
  }
  .band-green {
    position: absolute;
    top: 691px;
    left: 0;
    width: 100%;
    height: 47px;
    background: linear-gradient(90deg, var(--brand-green), var(--brand-green-light));
  }
  .clearance-badge {
    position: absolute;
    top: 574px;
    left: 131px;
    width: 168px;
    height: 168px;
  }
</style>
</head>
<body>
<main class="card-set">
  <section class="id-card id-card--front">
    <h1 class="brand-name">Bright<br>and Tidy</h1>
    <p class="website"><span class="part-blue">bright</span>and<span class="part-green">tidy</span>mn.example</p>
    <div class="employee-photo" role="img" aria-label="Employee portrait photo"></div>
    <h2 class="employee-name">Daniel Reyes</h2>
    <p class="employee-title">Managing Director</p>
    <div class="band-blue"></div>
    <div class="band-green"></div>
    <svg class="clearance-badge" viewBox="0 0 168 168" role="img" aria-label="Background check cleared badge">
      <circle cx="84" cy="84" r="83" fill="#ffffff"/>
      <circle cx="84" cy="84" r="72" fill="var(--brand-green)"/>
      <circle cx="84" cy="84" r="60" fill="#ffffff"/>
      <circle cx="84" cy="84" r="56" fill="var(--badge-dark)"/>
      <circle cx="84" cy="84" r="38" fill="none" stroke="var(--badge-gold)" stroke-width="3"/>
    </svg>
  </section>

  <section class="id-card id-card--back">
    <h1 class="brand-name">Bright<br>and Tidy</h1>
    <p class="website"><span class="part-blue">bright</span>and<span class="part-green">tidy</span>mn.example</p>
    <div class="employee-photo" role="img" aria-label="Employee portrait photo"></div>
    <h2 class="employee-name">Daniel Reyes</h2>
    <p class="employee-title">Managing Director</p>
    <div class="band-blue"></div>
    <div class="band-green"></div>
    <svg class="clearance-badge" viewBox="0 0 168 168" role="img" aria-label="Background check cleared badge">
      <circle cx="84" cy="84" r="83" fill="#ffffff"/>
      <circle cx="84" cy="84" r="72" fill="var(--brand-green)"/>
      <circle cx="84" cy="84" r="60" fill="#ffffff"/>
      <circle cx="84" cy="84" r="56" fill="var(--badge-dark)"/>
      <circle cx="84" cy="84" r="38" fill="none" stroke="var(--badge-gold)" stroke-width="3"/>
    </svg>
  </section>
</main>
</body>
</html>
```